パック詰めしたカニ身を入れる袋のデザインを依頼させていただきます。中の商品が見えるように、また通販のお客様だけでなく、デパートの食品売り場や高級スーパーで手にとっていただけるような、高級感のあるデザイン案をお願いします。イメージは『和モダン』です。
▼デザインの仕様▼
【袋サイズ】W200×H300(mm)
【デザインしていただく部分】W200×H270(mm)
※袋下30mmは空けておいてください。
商品が入った状態の参考画像は添付ファイル①を参照
(今回は袋のデザインをお願いします)
【色の数】4色まで
【材質】PP

▼記載内容▼※文字サイズ、字体、配置はおまかせいたします。
【商品名】右記よりどれか(かに身 ・ カニ身 ・ 蟹身)
【会社名】北岡商店
【賞味期限印刷用スペース】W30×H10(mm)※白抜きで
【商品特長】以下よりいくつか選択の上記載してください。
※表現は自由に変更してください。
・茹でへのこだわり(アルカリ水、瀬波の白粒使用)
・兵庫 香住港産
・日本海の深層水で育まれた
・みずみずしい
・カニ本来の甘み
【イメージ画像】添付ファイル②参照
※こちらは使っていただいてもいただかなくてもどちらでも結構です。
赤系、グレー系、黒・ゴールド等、高級感のある色
• 高解像度JPG (.jpg)
• イラストレーター形式 (.ai)
参考画像追記しておきます
多くのご提案ありがとうございます。
ご検討いただいているランサーの皆様に弊社よりお願いがあります。

1.依頼開始当初より記載しておりました、『和モダン』というイメージにあまり固執されすぎることなく、各ランサー様の自由な発想でデザインしていただきたい。
2.添付ファイル②のカニの画像は使用しないでください。

大変申し訳ございませんが、既にご提案いただいております皆様も、上記の点を踏まえまして、再度のご検討、ご提案いただければと思います。
残り日数少ない中、急な変更ではございますが何卒宜しくお願い致します。
上記変更に伴い、締め切りを1日延長させていただきます。
よろしくお願いいたします

ご質問等ございましたら、お気軽にお問い合わせ下さい。

・伝えたいことを見ただけで分かりやすくとらえることができる。
・主張しすぎないデザインの中に、高級感、上品さが感じ取れる。
・バランスがよく、中のカニ身を引き立ててくれると感じた。

皆様の貴重なお時間を、弊社依頼に費やしていただきまして、誠にありがとうございました。
今回見送らせていただいた皆様のご提案の中にも、素晴らしいデザインのものが数多くありました。今後もTesmora内におきまして他製品のパッケージやパンフレット等の依頼ができればと思っております。その際は是非また、素敵なご提案をお願いいたします。

```html
<!DOCTYPE html>
<html lang="ja">
<head>
<meta charset="utf-8">
<title>かに身 パッケージ</title>
<link href="https://fonts.googleapis.com/css2?family=Yuji+Syuku&family=Noto+Serif+JP:wght@500;700&family=Shippori+Mincho:wght@700&display=swap" rel="stylesheet">
<style>
  :root {
    --deep-red: #7a0a0c;
    --bright-red: #c8161b;
    --ink: #0d0505;
    --gold: #d8b25a;
    --gold-dark: #8c6a22;
    --pine: #1f6b3a;
    --white: #ffffff;
    --flesh-light: #f4e6d3;
    --flesh-red: #d9604a;
  }
  * { margin: 0; padding: 0; box-sizing: border-box; }
  html, body { width: 778px; height: 1200px; overflow: hidden; background: var(--ink); }
  .package {
    position: relative;
    width: 778px;
    height: 1200px;
    overflow: hidden;
    background:
      radial-gradient(ellipse 70% 55% at 50% 40%, var(--bright-red) 0%, var(--deep-red) 55%, var(--ink) 100%);
    font-family: "Noto Serif JP", serif;
  }
  .ornament {
    position: absolute;
    width: 150px;
    height: 200px;
    top: 20px;
    background: radial-gradient(ellipse at center, rgba(216,178,90,0.35), rgba(216,178,90,0) 70%);
  }
  .ornament--left { left: 10px; }
  .ornament--right { right: 10px; }
  .ornament--lower-left { left: 10px; top: 560px; }
  .ornament--lower-right { right: 10px; top: 820px; }
  .origin-banner {
    position: absolute;
    left: 233px; top: 13px;
    width: 312px; height: 66px;
    background: var(--pine);
    border: 4px solid var(--gold);
    box-shadow: 0 0 0 2px var(--gold-dark);
    color: var(--white);
    font-weight: 700;
    font-size: 36px;
    letter-spacing: 2px;
    display: flex; align-items: center; justify-content: center;
  }
  .product-window {
    position: absolute;
    left: 130px; top: 112px;
    width: 520px; height: 890px;
    border-radius: 34px;
    border: 6px solid var(--gold);
    box-shadow: 0 0 0 3px var(--gold-dark), 0 0 24px rgba(0,0,0,0.6);
    background:
      repeating-linear-gradient(90deg, var(--flesh-light) 0 38px, #f0c7b4 38px 52px, var(--flesh-red) 52px 60px, var(--flesh-light) 60px 80px);
    overflow: hidden;
  }
  .product-title {
    position: absolute;
    left: 260px; top: 250px;
    width: 260px; height: 740px;
    writing-mode: vertical-rl;
    font-family: "Yuji Syuku", serif;
    font-size: 236px;
    line-height: 1;
    color: var(--ink);
    text-align: center;
    -webkit-text-stroke: 14px var(--white);
    paint-order: stroke fill;
    display: flex; align-items: center; justify-content: center;
  }
  .maker-plate {
    position: absolute;
    left: 30px; top: 450px;
    width: 76px; height: 412px;
    background: var(--ink);
    border: 4px solid var(--gold);
    box-shadow: 0 0 0 2px var(--gold-dark);
    writing-mode: vertical-rl;
    color: var(--white);
    font-family: "Shippori Mincho", serif;
    font-weight: 700;
    font-size: 44px;
    letter-spacing: 6px;
    display: flex; align-items: center; justify-content: center;
  }
  .feature-copy {
    position: absolute;
    right: 16px; top: 128px;
    width: 100px; height: 760px;
    writing-mode: vertical-rl;
    color: var(--white);
    font-size: 29px;
    font-weight: 500;
    line-height: 1.35;
    text-shadow: 0 0 6px rgba(0,0,0,0.8);
  }
  .expiry-box {
    position: absolute;
    left: 556px; top: 985px;
    width: 196px; height: 54px;
    background: var(--white);
    border: 2px solid var(--ink);
    color: var(--ink);
    font-size: 18px;
    padding: 14px 0 0 14px;
  }
  .blank-strip {
    position: absolute;
    left: 0; bottom: 0;
    width: 778px; height: 125px;
    background: var(--ink);
  }
</style>
</head>
<body>
  <div class="package">
    <div class="ornament ornament--left" role="img" aria-label="金色の唐草飾り"></div>
    <div class="ornament ornament--right" role="img" aria-label="金色の唐草飾り"></div>
    <div class="ornament ornament--lower-left" role="img" aria-label="金色の唐草飾り"></div>
    <div class="ornament ornament--lower-right" role="img" aria-label="金色の唐草飾り"></div>

    <div class="origin-banner">兵庫 香住港産</div>

    <div class="product-window" role="img" aria-label="袋の窓から見えるカニ身の写真"></div>

    <h1 class="product-title">かに身</h1>

    <div class="maker-plate">北岡商店謹製</div>

    <p class="feature-copy">日本海の深層水で育まれた アルカリ水、瀬波の白粒で茹でられ、とれたての様にみずみずしく カニ本来の甘みが特徴です。</p>

    <div class="expiry-box">賞味期限</div>

    <div class="blank-strip"></div>
  </div>
</body>
</html>
```